Booth52 - iPad App Design Project

I have a iPad app that serves as a restaurant reservation system. The design that i currently have is very basic pearl design. I am looking for it to have a much more professional appeal.

Please review the attached document which contains all of the screen shots for the app.

This Project has now been Guaranteed.  I look forward to reviewing your designs.

Glen

Reason: I am extending my deadline because i just changed this contest to guaranteed and have received a ton more "acceptances" because of it and I want to give those designers a chance to submit a design.

Target Market(s)

restaurant owners

Industry/Entity Type

Restaurant

Requirements
Must have
• On the seating chart i am changing the feature that shows the tables highlighted and instead would like that replace with a badge. So the list of wait staff across the top of the seating chart would instead have a number next to their name and would correspond with the badge on the table to determine their section.

So for example:
Ana would have a number 1 in front of her name and tables 18, 19, 20, and 31 would have a little badge in the upper right hand corner with the number "1" inside the badge.
Tess would have a number 2 in front of her name and tables 6, 7, and 11 would have a little badge in the upper right hand corner with the number " 2" inside the badge.
Rita would have a number 3 in front of her name and tables 12, 13, 27, 28, 29, and 30 would have a little badge in the upper right hand corner with the number " 3" inside the badge.

The names on the top will all be ONE color

Also, i would like an icon developed to replace the "C" you see next to some of the people's name in the reservation and waitlist slots. Also, i would like a better looking "check mark".

```html
<!DOCTYPE html>
<html lang="en">
<head>
<meta charset="utf-8">
<title>Booth52 – Host Stand</title>
<link href="https://fonts.googleapis.com/css2?family=Open+Sans:wght@300;400;600;700&family=Ubuntu:wght@400;500;700&display=swap" rel="stylesheet">
<style>
  :root {
    --screen-top: #bdbdbd;
    --screen-bottom: #8e8e8e;
    --bar-light: #f4f4f4;
    --bar-mid: #d2d2d2;
    --bar-edge: #8a8a8a;
    --chip-bg: #6a6a6a;
    --chip-text: #f2f2f2;
    --chip-sub: #bdbdbd;
    --white: #ffffff;
    --ink: #4a4a4a;
    --ink-soft: #6d6d6d;
    --logo-blue: #2f8fd0;
    --card-dark: #555555;
    --card-fade: rgba(120,120,120,.55);
    --name-text: #e6e6e6;
    --meta-text: #b8b8b8;
    --wait-ok: #d6e04a;
    --wait-late: #e8a33c;
    --remove-red: #c8212b;
    --add-green: #2e9b34;
    --res-head-top: #6aa9e0;
    --res-head-bottom: #3f82c6;
    --res-body: #ececec;
    --res-ratio: #b5242b;
    --size-label: #3c5d80;
    --size-green: #4fae4f;
    --dash: #a8a8a8;
  }
  * { box-sizing: border-box; margin: 0; padding: 0; }
  html, body { width: 1200px; height: 815px; overflow: hidden; }
  body {
    font-family: "Open Sans", Arial, sans-serif;
    background: linear-gradient(180deg, var(--screen-top), var(--screen-bottom));
    position: relative;
  }

  /* header bar */
  .app-bar {
    position: absolute; left: 25px; top: 17px; width: 1115px; height: 66px;
    border-radius: 14px;
    background: linear-gradient(180deg, var(--bar-light), var(--bar-mid));
    border: 1px solid var(--bar-edge);
    box-shadow: inset 0 1px 0 #fff, 0 2px 4px rgba(0,0,0,.25);
  }
  .brand {
    position: absolute; left: 0; right: 0; top: 12px; text-align: center;
    font-weight: 300; font-size: 40px; line-height: 40px;
    color: var(--logo-blue); letter-spacing: -1px;
  }
  .bar-actions { position: absolute; right: 20px; top: 13px; display: flex; gap: 11px; }
  .bar-button {
    width: 58px; height: 38px; border-radius: 7px;
    background: linear-gradient(180deg, #7a7a7a, #4e4e4e);
    border: 1px solid #3a3a3a;
    display: flex; align-items: center; justify-content: center;
  }

  /* status row */
  .status-row { position: absolute; left: 31px; top: 97px; height: 44px; width: 1130px; }
  .clock {
    position: absolute; left: 0; top: 2px;
    font-family: "Ubuntu", Arial, sans-serif; font-weight: 700; font-size: 40px; line-height: 40px;
    color: var(--white); text-shadow: 0 1px 2px rgba(0,0,0,.35);
  }
  .meridiem {
    position: absolute; left: 130px; top: 4px;
    font-family: "Ubuntu", Arial, sans-serif; font-weight: 700; font-size: 14px; line-height: 17px;
    color: var(--white);
  }
  .meridiem .off { opacity: .8; }
  .divider { position: absolute; left: 160px; top: 2px; width: 5px; height: 40px; background: var(--white); }
  .date {
    position: absolute; left: 172px; top: 2px; text-align: center;
    font-family: "Ubuntu", Arial, sans-serif; font-weight: 700; font-size: 17px; line-height: 20px;
    color: var(--white);
  }
  .wait-chip {
    position: absolute; top: 0; width: 164px; height: 44px; border-radius: 6px;
    background: var(--chip-bg); text-align: center; padding-top: 3px;
    box-shadow: 0 1px 2px rgba(0,0,0,.3);
  }
  .wait-chip .label { font-family: "Ubuntu", Arial, sans-serif; font-weight: 700; font-size: 18px; color: var(--chip-text); line-height: 22px; }
  .wait-chip .value { font-size: 12px; color: var(--chip-sub); line-height: 14px; }
  .status-shadow {
    position: absolute; left: 25px; top: 148px; width: 1115px; height: 14px;
    background: radial-gradient(ellipse at top, rgba(60,60,60,.55), rgba(60,60,60,0) 70%);
  }

  /* wait list */
  .wait-list { position: absolute; left: 13px; top: 180px; width: 322px; }
  .wait-list-title {
    display: flex; align-items: center; gap: 10px; padding-left: 5px;
    font-family: "Ubuntu", Arial, sans-serif; font-weight: 700; font-size: 22px; color: var(--white);
    padding-bottom: 6px; border-bottom: 2px dashed rgba(255,255,255,.75); width: 310px;
  }
  .wait-card {
    position: absolute; left: 0; width: 322px; height: 86px; padding: 8px 0 0 12px;
    background: linear-gradient(90deg, var(--card-dark) 0%, var(--card-dark) 45%, var(--card-fade) 100%);
  }
  .wait-card .guest { font-size: 20px; font-weight: 300; color: var(--name-text); line-height: 24px; }
  .wait-card .party { font-size: 12px; color: var(--meta-text); line-height: 15px; }
  .wait-card .elapsed { font-size: 19px; color: var(--wait-ok); line-height: 24px; }
  .wait-card .elapsed.late { color: var(--wait-late); }
  .wait-card .remove { position: absolute; left: 285px; top: 30px; }

  /* reservations */
  .reservation-board {
    position: absolute; left: 355px; top: 186px; width: 806px; height: 640px;
    border-radius: 18px 18px 0 0;
    background: linear-gradient(180deg, rgba(255,255,255,.15), rgba(255,255,255,.05));
    border: 2px solid rgba(255,255,255,.85); border-bottom: none;
  }
  .res-card {
    position: absolute; width: 378px; height: 182px; border-radius: 6px; overflow: hidden;
    background: var(--res-body); border: 2px solid #9a9a9a;
    box-shadow: 0 2px 5px rgba(0,0,0,.35);
  }
  .res-head {
    position: relative; height: 45px;
    background: linear-gradient(180deg, var(--res-head-top), var(--res-head-bottom));
  }
  .res-head .slot {
    position: absolute; left: 14px; top: 8px;
    font-family: "Ubuntu", Arial, sans-serif; font-weight: 700; font-size: 21px; color: #f0f0f0;
    text-shadow: 0 1px 2px rgba(0,0,0,.55);
  }
  .res-head .ratio { position: absolute; left: 155px; top: 15px; font-size: 12px; color: var(--res-ratio); }
  .res-head .size-label { position: absolute; left: 238px; top: 11px; font-size: 16px; color: var(--size-label); }
  .res-head .add { position: absolute; right: 10px; top: 10px; }
  .res-body { position: relative; height: 133px; }
  .res-body::after {
    content: ""; position: absolute; left: 275px; top: 0; bottom: 0;
    border-left: 1px dashed var(--dash);
  }
  .res-row { position: absolute; left: 12px; width: 250px; }
  .res-row .party-name { font-size: 17px; color: var(--ink); line-height: 20px; }
  .res-row .note { font-size: 10px; color: var(--ink-soft); line-height: 12px; }
  .res-row .count { position: absolute; left: 232px; top: 0; font-size: 19px; color: var(--size-green); line-height: 22px; }
</style>
</head>
<body>

<header class="app-bar">
  <div class="brand">Booth52</div>
  <div class="bar-actions">
    <div class="bar-button" aria-label="Reservation book">
      <svg width="32" height="24" viewBox="0 0 32 24"><path d="M16 5 C12 2 6 2 2 4 V21 C6 19 12 19 16 22 C20 19 26 19 30 21 V4 C26 2 20 2 16 5 Z M16 5 V22" fill="none" stroke="#fff" stroke-width="2.2" stroke-linejoin="round"/></svg>
    </div>
    <div class="bar-button" aria-label="Edit">
      <svg width="28" height="26" viewBox="0 0 28 26"><rect x="3" y="5" width="18" height="18" fill="none" stroke="#fff" stroke-width="2.2"/><path d="M11 16 L12 12 L23 2 L26 5 L15 15 Z" fill="#fff"/></svg>
    </div>
  </div>
</header>

<section class="status-row">
  <div class="clock">09:00</div>
  <div class="meridiem"><div class="off">AM</div><div>PM</div></div>
  <div class="divider"></div>
  <div class="date">26 MAY<br>2012</div>
  <div class="wait-chip" style="left:281px"><div class="label">Avg Wait Time</div><div class="value">25 mins</div></div>
  <div class="wait-chip" style="left:464px"><div class="label">Avg Wait Time</div><div class="value">25 mins</div></div>
  <div class="wait-chip" style="left:661px"><div class="label">Avg Wait Time</div><div class="value">25 mins</div></div>
  <div class="wait-chip" style="left:854px"><div class="label">Avg Wait Time</div><div class="value">25 mins</div></div>
</section>
<div class="status-shadow"></div>

<aside class="wait-list">
  <div class="wait-list-title">
    <svg width="36" height="36" viewBox="0 0 36 36"><circle cx="18" cy="18" r="16" fill="var(--add-green)" stroke="#fff" stroke-width="3"/><path d="M18 9 V27 M9 18 H27" stroke="#fff" stroke-width="5"/></svg>
    Wait List
  </div>
  <div class="wait-card" style="top:49px"><div class="guest">Clara Bennett</div><div class="party">Party of 4</div><div class="elapsed">5m (2:02 PM)</div>
    <svg class="remove" width="28" height="28" viewBox="0 0 28 28"><circle cx="14" cy="14" r="12" fill="var(--remove-red)" stroke="#fff" stroke-width="2.5"/><rect x="7" y="12" width="14" height="4" fill="#fff"/></svg></div>
  <div class="wait-card" style="top:148px"><div class="guest">Clara Bennett</div><div class="party">Party of 4</div><div class="elapsed">5m (2:02 PM)</div>
    <svg class="remove" width="28" height="28" viewBox="0 0 28 28"><circle cx="14" cy="14" r="12" fill="var(--remove-red)" stroke="#fff" stroke-width="2.5"/><rect x="7" y="12" width="14" height="4" fill="#fff"/></svg></div>
  <div class="wait-card" style="top:247px"><div class="guest">Clara Bennett</div><div class="party">Party of 4</div><div class="elapsed late">5m (2:02 PM)</div>
    <svg class="remove" width="28" height="28" viewBox="0 0 28 28"><circle cx="14" cy="14" r="12" fill="var(--remove-red)" stroke="#fff" stroke-width="2.5"/><rect x="7" y="12" width="14" height="4" fill="#fff"/></svg></div>
  <div class="wait-card" style="top:346px"><div class="guest">Clara Bennett</div><div class="party">Party of 4</div><div class="elapsed">5m (2:02 PM)</div>
    <svg class="remove" width="28" height="28" viewBox="0 0 28 28"><circle cx="14" cy="14" r="12" fill="var(--remove-red)" stroke="#fff" stroke-width="2.5"/><rect x="7" y="12" width="14" height="4" fill="#fff"/></svg></div>
  <div class="wait-card" style="top:445px"><div class="guest">Clara Bennett</div><div class="party">Party of 4</div><div class="elapsed">5m (2:02 PM)</div>
    <svg class="remove" width="28" height="28" viewBox="0 0 28 28"><circle cx="14" cy="14" r="12" fill="var(--remove-red)" stroke="#fff" stroke-width="2.5"/><rect x="7" y="12" width="14" height="4" fill="#fff"/></svg></div>
</aside>

<main class="reservation-board">
  <article class="res-card" style="left:17px;top:19px">
    <div class="res-head"><span class="slot">12:15</span><span class="ratio">7/20</span><span class="size-label">Size</span>
      <svg class="add" width="24" height="24" viewBox="0 0 24 24"><path d="M12 2 V22 M2 12 H22" stroke="#fff" stroke-width="4.5"/></svg></div>
    <div class="res-body">
      <div class="res-row" style="top:5px"><div class="party-name">Lorem Ipsum</div><div class="note">Patio table if possible</div><span class="count" style="top:6px">3</span></div>
      <div class="res-row" style="top:48px"><div class="party-name">Lorem Ipsum</div><span class="count">4</span></div>
      <div class="res-row" style="top:86px"><div class="party-name">Lorem Ipsum</div><span class="count">3</span></div>
    </div>
  </article>
  <article class="res-card" style="left:408px;top:19px">
    <div class="res-head"><span class="slot">12:15</span><span class="ratio">7/20</span><span class="size-label">Size</span>
      <svg class="add" width="24" height="24" viewBox="0 0 24 24"><path d="M12 2 V22 M2 12 H22" stroke="#fff" stroke-width="4.5"/></svg></div>
    <div class="res-body">
      <div class="res-row" style="top:5px"><div class="party-name">Lorem Ipsum</div><div class="note">Patio table if possible</div><span class="count" style="top:6px">3</span></div>
      <div class="res-row" style="top:48px"><div class="party-name">Lorem Ipsum</div><span class="count">4</span></div>
      <div class="res-row" style="top:86px"><div class="party-name">Lorem Ipsum</div><span class="count">3</span></div>
    </div>
  </article>
  <article class="res-card" style="left:17px;top:219px">
    <div class="res-head"><span class="slot">12:15</span><span class="ratio">7/20</span><span class="size-label">Size</span>
      <svg class="add" width="24" height="24" viewBox="0 0 24 24"><path d="M12 2 V22 M2 12 H22" stroke="#fff" stroke-width="4.5"/></svg></div>
    <div class="res-body">
      <div class="res-row" style="top:5px"><div class="party-name">Lorem Ipsum</div><div class="note">Patio table if possible</div><span class="count" style="top:6px">3</span></div>
      <div class="res-row" style="top:48px"><div class="party-name">Lorem Ipsum</div><span class="count">4</span></div>
      <div class="res-row" style="top:86px"><div class="party-name">Lorem Ipsum</div><span class="count">3</span></div>
    </div>
  </article>
  <article class="res-card" style="left:408px;top:219px">
    <div class="res-head"><span class="slot">12:15</span><span class="ratio">7/20</span><span class="size-label">Size</span>
      <svg class="add" width="24" height="24" viewBox="0 0 24 24"><path d="M12 2 V22 M2 12 H22" stroke="#fff" stroke-width="4.5"/></svg></div>
    <div class="res-body">
      <div class="res-row" style="top:5px"><div class="party-name">Lorem Ipsum</div><div class="note">Patio table if possible</div><span class="count" style="top:6px">3</span></div>
      <div class="res-row" style="top:48px"><div class="party-name">Lorem Ipsum</div><span class="count">4</span></div>
      <div class="res-row" style="top:86px"><div class="party-name">Lorem Ipsum</div><span class="count">3</span></div>
    </div>
  </article>
  <article class="res-card" style="left:17px;top:418px">
    <div class="res-head"><span class="slot">12:15</span><span class="ratio">7/20</span><span class="size-label">Size</span>
      <svg class="add" width="24" height="24" viewBox="0 0 24 24"><path d="M12 2 V22 M2 12 H22" stroke="#fff" stroke-width="4.5"/></svg></div>
    <div class="res-body">
      <div class="res-row" style="top:5px"><div class="party-name">Lorem Ipsum</div><div class="note">Patio table if possible</div><span class="count" style="top:6px">3</span></div>
      <div class="res-row" style="top:48px"><div class="party-name">Lorem Ipsum</div><span class="count">4</span></div>
      <div class="res-row" style="top:86px"><div class="party-name">Lorem Ipsum</div><span class="count">3</span></div>
    </div>
  </article>
  <article class="res-card" style="left:408px;top:418px">
    <div class="res-head"><span class="slot">12:15</span><span class="ratio">7/20</span><span class="size-label">Size</span>
      <svg class="add" width="24" height="24" viewBox="0 0 24 24"><path d="M12 2 V22 M2 12 H22" stroke="#fff" stroke-width="4.5"/></svg></div>
    <div class="res-body">
      <div class="res-row" style="top:5px"><div class="party-name">Lorem Ipsum</div><div class="note">Patio table if possible</div><span class="count" style="top:6px">3</span></div>
      <div class="res-row" style="top:48px"><div class="party-name">Lorem Ipsum</div><span class="count">4</span></div>
      <div class="res-row" style="top:86px"><div class="party-name">Lorem Ipsum</div><span class="count">3</span></div>
    </div>
  </article>
</main>

</body>
</html>
```